Pet Shop Website

website will need to have the following features:
• Photo Galleries of each species (Dogs, Cats, Birds, Fish, Reptiles, Rabbits) in a light box popup
o Each species may have several different categories for example:
 Fish
• Marine fish
• Fresh water
• tropical
• Cichlid
• Information Fact sheets of each species – Downloaded as a pdf which can be either
o Care Sheets
o Training Sheets
• Members Area
o Username (Email Address) & Password login
o New signups
o Exclusive Member Deals
o Newsletter options

The front page must be very simple (for example lumavest.com.au) contain the following:
• Product of the week - which can be purchased online
o Short details
o Cost
• Pet Club Sign up picture
• Animal of the week/month
• Contact Phone Number and addresses of the stores
• A jQuery slideshow (Images could include stores, pets etc…)
The main page MUST keep simple. We do not want it cluttered.

Inner Page
The animals / reptile page will need to have:
• Short description of the species
• Photo Galleries
• A list of what is in stock and the list needs to clearly be sorted by each store (Use of Tabs maybe).
• Facts sheets / Info sheets
The type of website ideas (not the type of look that we are necessary after) is and the sort of content that we want to offer are as follows:

http://www.scalenook.com.au/
http://www.brindlecovepaws.com.au/
http://www.thefurrowden.com.au
http://www.tailtown.net.au

Colour in the new website:
Blue
Red
Grey
Yellow

Original site:

http://www.critterglow.com.au
Updates

Hi Guys,

We had feedback from the client and they would like to see a few dark designs.

Thanks                                   

Reason: We would like to reopen this contest back up for a further week

Target Market(s)

Targeting animal lovers

Industry/Entity Type

Store

Requirements
Should not have
• Alter the logo in anyway

```html
<!DOCTYPE html>
<html lang="en">
<head>
<meta charset="utf-8">
<title>Critter Glow – Pet Superstores</title>
<link href="https://fonts.googleapis.com/css2?family=Source+Sans+3:wght@400;600&display=swap" rel="stylesheet">
<style>
:root{
  --navy:#0c0e5a;
  --nav:#2c2589;
  --ink:#1c1a6a;
  --text:#555;
  --muted:#888;
  --yellow:#f3d36b;
  --red:#b01515;
  --card-border:#dcdcdc;
  --btn:#0d0f45;
  --white:#fff;
}
*{box-sizing:border-box;margin:0;padding:0}
html,body{width:890px;height:1200px;overflow:hidden}
body{background:var(--navy);font-family:"Source Sans 3",sans-serif;position:relative;color:var(--text)}
.abs{position:absolute}
.page{left:35px;top:16px;width:820px;height:1042px;background:var(--white)}
.brand{left:61px;top:62px;display:flex;align-items:center;gap:10px;font-size:34px;font-weight:600;color:var(--nav)}
.brand .dot{width:26px;height:26px;border-radius:50%;background:var(--yellow)}
.search{left:634px;top:29px;width:190px;height:25px;background:var(--nav);color:#fff;font-size:12px;padding:4px 12px;border:1px solid #6c68b8}
.search svg{position:absolute;right:7px;top:5px}
.mascot{left:634px;top:94px;width:48px;height:43px;background:linear-gradient(#f4f4f4,#d6d6d6);border-radius:50% 50% 6px 6px}
.phone{left:691px;top:100px;font-size:20px;color:#2a4f9a}
.nav{left:35px;top:138px;width:820px;height:34px;background:var(--nav);display:flex;align-items:center}
.nav a{position:absolute;color:#fff;font-size:13px;text-decoration:none}
.nav .home{left:10px;top:3px;width:68px;height:27px;background:var(--yellow);color:var(--nav);border-radius:3px;display:flex;align-items:center;justify-content:center}
.slider{left:42px;top:187px;width:810px;height:260px;background:linear-gradient(90deg,#ececec,#fafafa 50%,#e6e6e6);border-radius:4px;overflow:hidden}
.slider .photo-left{left:60px;top:0;width:250px;height:260px;background:radial-gradient(ellipse at 50% 45%,#d9a35c,#e8cfa4 55%,transparent 72%)}
.slider .photo-right{left:555px;top:0;width:255px;height:260px;background:radial-gradient(ellipse at 45% 70%,#dfe6ea,#c9d3d8 40%,transparent 55%),radial-gradient(ellipse at 80% 25%,#e3a35e,transparent 45%)}
.slider h1{left:283px;top:93px;font-weight:400;font-size:21px;line-height:31px;color:var(--ink)}
.slide-shadow{left:60px;top:447px;width:770px;height:16px;background:radial-gradient(ellipse at 50% 0,rgba(0,0,0,.25),transparent 70%)}
.arrow{position:absolute}
.card{background:#fff;border:1px solid var(--card-border);border-radius:3px;box-shadow:0 1px 3px rgba(0,0,0,.12)}
.login{left:42px;top:492px;width:213px;height:153px}
.login .head{height:32px;border-bottom:1px solid #eee;background:linear-gradient(#fff,#f1f1f1);display:flex;align-items:center;padding-left:42px;color:var(--ink);font-size:13px}
.login .avatar{position:absolute;left:10px;top:5px;width:22px;height:22px;background:#555;border-radius:3px}
.login label{position:absolute;font-size:9px;color:var(--muted);left:18px}
.login input{position:absolute;left:76px;width:111px;height:19px;border:1px solid #bbb;background:#e9e9e9}
.btn{position:absolute;background:var(--btn);color:#fff;font-size:11px;display:flex;align-items:center;justify-content:center;border-radius:2px}
.promo{border:2px solid var(--nav);border-radius:3px;overflow:hidden}
.deals{left:284px;top:492px;width:261px;height:152px;background:linear-gradient(135deg,#5f8f3a,#c9a16a 50%,#7aa24a)}
.club{left:571px;top:492px;width:261px;height:152px;background:linear-gradient(135deg,#c9d3e0,#d8a66c 45%,#e4e8ef)}
.promo .title{position:absolute;left:16px;top:10px;font-size:15px}
.deals .title{color:#fff}
.club .title{color:var(--red)}
.promo .cta{position:absolute;right:0;bottom:0;background:rgba(255,255,255,.7);color:var(--red);font-size:11px;padding:5px 4px 4px 10px}
.sheets{left:44px;top:668px;width:213px;height:154px}
.sheet{position:absolute;left:26px;display:flex;gap:16px}
.sheet .icon{width:39px;height:39px;background:#c81e1e;border-radius:2px}
.sheet b{display:block;font-weight:400;font-size:12px;color:#333;margin-top:4px}
.sheet span{font-size:10px;color:var(--muted)}
.newsletter{left:44px;top:843px;width:213px;height:154px}
.newsletter h2{position:absolute;left:24px;top:18px;font-weight:400;font-size:16px;color:var(--ink)}
.newsletter .email{position:absolute;left:15px;top:54px;width:186px;height:22px;border:1px solid #bbb;font-size:9px;font-style:italic;padding:4px 16px;color:#555}
.newsletter .subscribe{left:97px;top:94px;width:103px;height:27px;font-size:12px;border-radius:4px;background:linear-gradient(#2a3aa0,#0d1566)}
.panel{background:#fafafa;border:1px solid #eee}
.product{left:282px;top:668px;width:186px;height:222px}
.animal{left:491px;top:668px;width:345px;height:222px}
.panel h3{position:absolute;font-weight:400;font-size:16px;color:var(--ink)}
.ph{position:absolute}
.rabbit-white{background:linear-gradient(160deg,#4e6a3a,#e9ecef 55%,#b79c72)}
.rabbit-pair{background:radial-gradient(ellipse at 50% 60%,#9c8774,#f3f3f3 60%)}
.rabbit-tan{background:radial-gradient(ellipse at 50% 65%,#d0a06a,#f3f3f3 60%)}
.lorem{position:absolute;font-size:9.5px;line-height:15.5px;color:#666}
.gallery-title{left:286px;top:904px;font-size:16px;color:#333}
.gphoto{position:absolute;top:939px;width:138px;height:95px;border-radius:3px;box-shadow:0 2px 4px rgba(0,0,0,.25)}
.bird{left:320px;background:linear-gradient(135deg,#9aa48a,#6f8a5a)}
.lizard{left:490px;background:linear-gradient(135deg,#3c5a2a,#b9b040 55%,#2d4420)}
.fish{left:660px;background:linear-gradient(135deg,#1a4fa0,#f0c030 55%,#1a3a80)}
.footer{color:#fff}
.footer h4{left:43px;top:1074px;font-weight:400;font-size:16px}
.addr{font-size:11px;line-height:20px;top:1106px}
.social{left:743px;top:1096px;display:flex;gap:5px}
.social i{width:22px;height:22px;border-radius:3px;display:block}
.copy{right:42px;top:1132px;font-size:10px}
</style>
</head>
<body>
<div class="abs page"></div>

<div class="abs brand"><span class="dot"></span>Critter Glow</div>
<div class="abs search">Search
  <svg width="13" height="13" viewBox="0 0 13 13"><circle cx="5.5" cy="5.5" r="4.3" fill="none" stroke="#fff" stroke-width="1.4"/><path d="M8.6 8.6 12 12" stroke="#fff" stroke-width="1.6"/></svg>
</div>
<div class="abs mascot" role="img" aria-label="Dog mascot wearing a headset"></div>
<div class="abs phone">(08) 9000 1420</div>

<nav class="abs nav">
  <a class="home" href="#">Home</a>
  <a href="#" style="left:105px;top:10px">About Us</a>
  <a href="#" style="left:193px;top:10px">Pets</a>
  <a href="#" style="left:263px;top:10px">Contact Us</a>
</nav>

<section class="abs slider">
  <div class="abs photo-left" role="img" aria-label="Golden retriever sitting"></div>
  <div class="abs photo-right" role="img" aria-label="Kitten leaning on a fishbowl with a goldfish"></div>
  <h1 class="abs">Critter Glow your<br>PET SUPERSTORES at<br>Elmswood and Ashgrove</h1>
  <svg class="arrow" style="left:13px;top:116px" width="22" height="42"><path d="M19 2 4 21 19 40" fill="none" stroke="#888" stroke-width="3"/></svg>
  <svg class="arrow" style="left:778px;top:116px" width="22" height="42"><path d="M3 2 18 21 3 40" fill="none" stroke="#fff" stroke-width="3"/></svg>
</section>
<div class="abs slide-shadow"></div>

<section class="abs card login">
  <div class="head"><span class="avatar"></span>LOGIN</div>
  <label style="top:53px">User Name :</label><input style="top:45px" aria-label="User Name">
  <label style="top:85px">Password :</label><input style="top:77px" type="password" aria-label="Password">
  <div class="btn" style="left:78px;top:110px;width:60px;height:21px">Submit</div>
</section>

<section class="abs promo deals" role="img" aria-label="Woman hugging a golden retriever and a cat">
  <div class="title">EXCLUSIVE MEMBER DEALS</div>
  <div class="cta">CLICK HERE &gt;&gt;</div>
</section>
<section class="abs promo club" role="img" aria-label="Two lop-eared rabbits in a towel">
  <div class="title">PET CLUB</div>
  <div class="cta">SIGN UP NOW &gt;&gt;</div>
</section>

<section class="abs card sheets">
  <div class="sheet" style="top:28px"><div class="icon"></div><div><b>CARE SHEETS</b><span>Download Here &gt;&gt;</span></div></div>
  <div class="sheet" style="top:81px"><div class="icon"></div><div><b>TRAINING SHEETS</b><span>Download Here &gt;&gt;</span></div></div>
</section>

<section class="abs card newsletter">
  <h2>Newsletter</h2>
  <div class="email">Enter Your Email</div>
  <div class="btn subscribe">SUBSCRIBE</div>
</section>

<section class="abs panel product">
  <h3 style="left:8px;top:6px">Product of the week</h3>
  <div class="ph rabbit-white" style="left:6px;top:35px;width:170px;height:106px" role="img" aria-label="Two white rabbits"></div>
  <p class="lorem" style="left:14px;top:156px">Lorem ipsum dolor sit amet,<br>consectetur adipiscing elit.</p>
  <div class="btn" style="left:79px;top:184px;width:88px;height:24px">BUY NOW &nbsp;&gt;&gt;</div>
</section>

<section class="abs panel animal">
  <h3 style="left:12px;top:11px">Animal of the week</h3>
  <div class="ph rabbit-pair" style="left:29px;top:42px;width:120px;height:99px" role="img" aria-label="Two rabbits sitting side by side"></div>
  <div class="ph rabbit-tan" style="left:178px;top:42px;width:139px;height:99px" role="img" aria-label="Two tan rabbits nuzzling"></div>
  <p class="lorem" style="left:30px;top:154px">Lorem ipsum dolor sit amet,<br>consectetur adipiscing elit.</p>
  <p class="lorem" style="left:181px;top:154px">Lorem ipsum dolor sit amet,<br>consectetur adipiscing elit.</p>
  <div class="btn" style="left:28px;top:184px;width:70px;height:24px">Details</div>
  <div class="btn" style="left:193px;top:184px;width:70px;height:24px">Details</div>
</section>

<div class="abs gallery-title">PhotoGallery</div>
<svg class="arrow" style="left:289px;top:975px" width="16" height="30"><path d="M14 2 3 15 14 28" fill="none" stroke="#777" stroke-width="2"/></svg>
<div class="gphoto bird" role="img" aria-label="Hummingbird in flight"></div>
<div class="gphoto lizard" role="img" aria-label="Lizard on a branch"></div>
<div class="gphoto fish" role="img" aria-label="Striped angelfish"></div>
<svg class="arrow" style="left:819px;top:975px" width="16" height="30"><path d="M2 2 13 15 2 28" fill="none" stroke="#777" stroke-width="2"/></svg>

<footer class="footer">
  <h4 class="abs">Store Location</h4>
  <p class="abs addr" style="left:43px">Shop 4 / 220 Harbour Rd<br>ELMSWOOD W.A 6102<br>Phone: (08) 9000 1420<br>Fax: (08) 9000 1430</p>
  <p class="abs addr" style="left:209px">Unit 3 / 18 Meridian Drive<br>ASHGROVE W.A 6160<br>Phone: (08) 9000 2210<br>Fax: (08) 9000 2230</p>
  <div class="abs social" aria-label="Social links">
    <i style="background:#3b5aa0"></i><i style="background:#33a9e0"></i><i style="background:#1b7ab8"></i><i style="background:#f08a1c"></i>
  </div>
  <p class="abs copy">© 2012 critterglow, All Rights Reserved</p>
</footer>
</body>
</html>
```